コンペの提出はファーストビューのみでも大丈夫です。
金額はLP全てのデザイン分です。
納品はXDもしくはPSDでお願いいたします。

【ターゲット】
30-50代の男女向け 男女比率 女性7:男性3

【デザインテイストについて】
反響の良かったチラシをベースに原稿制作しました。
添付しておきますのでデザインテイストについても参考にしていただいて問題ありません。

その他デザイン参考サイト
https://tokiwa-partners.co.jp/career-tag/occupation/r50_a

【写真素材】
https://share.kumofiles-box.net/drive/folders/7qTwMxLpeRsVa2Hc9NjUbZo4KdFgiYwAe?usp=sharing

足りない写真素材はピクセリアフォトなどを使用してください
ロゴデータは添付してあります
1ページ
青系
原稿兼WFを添付します。

WFについては目安として考えていただき、デザインアイデアで変更していただいても大丈夫です。

要望通りのデザインを作成していただきありがとうございました!

限られた時間の中で多くのご提案をいただきまして本当にありがとうございました。
また機会がありましたらよろしくお願いいたします。

```html
<!DOCTYPE html>
<html lang="ja">
<head>
<meta charset="utf-8">
<title>登録ヘルパー大募集</title>
<link rel="stylesheet" href="https://fonts.googleapis.com/css2?family=M+PLUS+Rounded+1c:wght@500;700;800&display=swap">
<style>
:root{
  --sky:#bfe6f7;
  --sky-deep:#a9dcf2;
  --navy:#1f3f86;
  --blue:#1a7fc8;
  --pink:#f0447c;
  --green:#2bb24c;
  --ink:#23324f;
  --white:#ffffff;
}
*{margin:0;padding:0;box-sizing:border-box}
html,body{width:1200px;height:2768px;overflow:hidden;background:var(--white)}
body{font-family:"M PLUS Rounded 1c",sans-serif;color:var(--ink);position:relative}
.hero{position:absolute;left:0;top:0;width:1200px;height:610px;background:linear-gradient(180deg,var(--sky) 0%,var(--sky-deep) 100%)}
.brand{position:absolute;left:28px;top:18px;width:120px;display:flex;flex-direction:column;align-items:center;gap:6px}
.brand-dot{width:52px;height:52px;border-radius:50%;background:var(--blue)}
.brand-name{font-size:28px;font-weight:800;color:var(--blue);line-height:1}
.area{position:absolute;left:170px;width:860px;top:30px;text-align:center;font-size:29px;font-weight:700;color:var(--navy);white-space:nowrap}
.headline{position:absolute;left:150px;width:900px;top:78px;text-align:center;font-size:84px;line-height:100px;font-weight:800;color:var(--pink);letter-spacing:2px;white-space:nowrap;text-shadow:4px 4px 0 var(--white),-4px -4px 0 var(--white),4px -4px 0 var(--white),-4px 4px 0 var(--white),0 4px 0 var(--white),0 -4px 0 var(--white)}
.team-photo{position:absolute;left:195px;top:185px;width:800px;height:245px;border-radius:125px;border:8px solid var(--navy);background:linear-gradient(180deg,#e9eef2 0%,#cfdde6 55%,#9fd8d6 100%)}
.wishes{position:absolute;left:130px;top:440px;width:250px;padding:10px 14px;background:var(--white);border-radius:12px;list-style:none;box-shadow:0 2px 6px rgba(0,0,0,.08)}
.wishes li{display:flex;align-items:center;gap:8px;font-size:19px;font-weight:700;line-height:30px;color:var(--ink);white-space:nowrap}
.wishes svg{flex:none}
.pay{position:absolute;top:455px;display:flex;align-items:center;gap:10px}
.pay-day{left:410px}
.pay-night{left:720px}
.pay-tag{display:flex;flex-direction:column;align-items:center;justify-content:center;color:var(--white);border-radius:6px;padding:4px 12px;height:54px}
.pay-tag b{font-size:24px;line-height:26px;white-space:nowrap}
.pay-tag small{font-size:11px}
.pay-day .pay-tag{background:var(--pink)}
.pay-night .pay-tag{background:var(--blue)}
.pay-rate{font-size:21px;font-weight:700;color:var(--ink);white-space:nowrap}
.pay-rate strong{font-size:34px;font-weight:800}
.pay-day .pay-rate strong{color:var(--pink)}
.pay-night .pay-rate strong{color:var(--blue)}
.pay-box{display:flex;align-items:center;gap:10px;background:var(--white);padding:4px 14px 4px 4px;border-radius:8px}
.all-ok{position:absolute;left:455px;top:528px;font-size:36px;font-weight:800;color:var(--pink);white-space:nowrap}
.side-actions{position:absolute;right:0;top:40px;width:62px;display:flex;flex-direction:column;gap:6px}
.side-btn{display:flex;flex-direction:column;align-items:center;justify-content:center;border-radius:10px 0 0 10px;color:var(--white)}
.side-mail{height:180px;background:var(--blue);gap:8px}
.side-mail span{writing-mode:vertical-rl;font-size:20px;font-weight:700}
.side-phone{height:58px;background:var(--blue)}
.side-chat{height:58px;background:var(--green)}
.chat-square{width:28px;height:28px;border-radius:6px;background:var(--white)}
</style>
</head>
<body>
<section class="hero">
  <div class="brand"><span class="brand-dot"></span><span class="brand-name">ひなた</span></div>
  <p class="area">宜野湾・浦添・うるま・中城・沖縄・北谷周辺で直行直帰！</p>
  <h1 class="headline">登録ヘルパー大募集！</h1>
  <div class="team-photo" role="img" aria-label="揃いのユニフォームを着たスタッフの集合写真"></div>

  <ul class="wishes">
    <li><svg width="18" height="18" viewBox="0 0 18 18"><path d="M2 9l5 5 9-10" fill="none" stroke="#1a7fc8" stroke-width="3"/></svg>月収35万円以上希望</li>
    <li><svg width="18" height="18" viewBox="0 0 18 18"><path d="M2 9l5 5 9-10" fill="none" stroke="#1a7fc8" stroke-width="3"/></svg>扶養内で働きたい</li>
    <li><svg width="18" height="18" viewBox="0 0 18 18"><path d="M2 9l5 5 9-10" fill="none" stroke="#1a7fc8" stroke-width="3"/></svg>夜間にWワークしたい</li>
    <li><svg width="18" height="18" viewBox="0 0 18 18"><path d="M2 9l5 5 9-10" fill="none" stroke="#1a7fc8" stroke-width="3"/></svg>身体介護は避けたい</li>
    <li><svg width="18" height="18" viewBox="0 0 18 18"><path d="M2 9l5 5 9-10" fill="none" stroke="#1a7fc8" stroke-width="3"/></svg>希望の日に休みたい</li>
  </ul>

  <div class="pay pay-day"><div class="pay-box"><div class="pay-tag"><b>日勤</b><small>9:00-18:00</small></div><p class="pay-rate">時給 <strong>1,500</strong>円</p></div></div>
  <div class="pay pay-night"><div class="pay-box"><div class="pay-tag"><b>夜・日祝</b><small>6:00-18:00</small></div><p class="pay-rate">時給 <strong>1,875</strong>円</p></div></div>

  <p class="all-ok">全部OK！ 都合に合わせて働けます！</p>
</section>

<nav class="side-actions">
  <a class="side-btn side-mail"><svg width="28" height="20" viewBox="0 0 28 20"><rect x="1" y="1" width="26" height="18" rx="2" fill="#fff"/><path d="M2 2l12 9 12-9" fill="none" stroke="#1a7fc8" stroke-width="2"/></svg><span>応募する</span></a>
  <a class="side-btn side-phone"><svg width="26" height="26" viewBox="0 0 24 24"><path d="M6.6 10.8a15 15 0 006.6 6.6l2.2-2.2a1 1 0 011-.25 11.4 11.4 0 003.6.57 1 1 0 011 1V20a1 1 0 01-1 1A17 17 0 013 4a1 1 0 011-1h3.5a1 1 0 011 1c0 1.25.2 2.45.57 3.6a1 1 0 01-.25 1z" fill="#fff"/></svg></a>
  <a class="side-btn side-chat"><span class="chat-square"></span></a>
</nav>
</body>
</html>
```